Business Card Design

I am nail technician working from home in Fernwick Rise, Perth and I require new business cards. I only work with Gel medium for nail extensions using tips or I can also do sculpture nails. I specialise in hand painted nail art using water based acrylic paint and nail polish. As the name suggest I love all things "Shimmer" so I would love something that reflects this while also being professional. I'm also on Chatterly and would the Chatterly logo.

Contact Information for Business Card

Shimmer Bay nail designs,Rosanne ,0417859263, ShimmerBaynaildesigns@quellmail.com, nail technician specialising in hand painted nail art, only using a Gel medium

```html
<!DOCTYPE html>
<html lang="en">
<head>
<meta charset="utf-8">
<title>Shimmer Bay Nail Designs – Business Card</title>
<link rel="stylesheet" href="https://fonts.googleapis.com/css2?family=Questrial&display=swap">
<style>
  :root {
    --page-bg: #e9e9ea;
    --card-red: #d2282b;
    --card-red-light: #de4a4c;
    --silver: #e8e6e2;
    --card-white: #ffffff;
    --text-grey: #6e6e70;
    --shadow: rgba(0, 0, 0, 0.18);
  }
  * { box-sizing: border-box; margin: 0; padding: 0; }
  html, body {
    width: 1200px;
    height: 1000px;
    overflow: hidden;
    background: var(--page-bg);
    font-family: "Questrial", "Century Gothic", sans-serif;
  }
  .sheet {
    width: 1200px;
    height: 1000px;
    display: flex;
    flex-direction: column;
    align-items: center;
    justify-content: center;
    gap: 44px;
  }
  .card {
    width: 760px;
    height: 434px;
    border-radius: 22px;
    box-shadow: 0 10px 28px var(--shadow);
    overflow: hidden;
    position: relative;
  }

  /* Back of card */
  .card-back {
    background: var(--card-red);
    display: flex;
    flex-direction: column;
    justify-content: space-between;
  }
  .swirl-band {
    height: 130px;
    width: 100%;
  }
  .swirl-band--top {
    background: linear-gradient(180deg, var(--card-red-light) 0%, var(--card-red) 100%);
  }
  .swirl-band--bottom {
    background: linear-gradient(0deg, var(--card-red-light) 0%, var(--card-red) 100%);
  }
  .tagline {
    color: var(--silver);
    font-size: 23px;
    letter-spacing: 2px;
    line-height: 1.75;
    text-align: center;
  }

  /* Front of card */
  .card-front {
    background: var(--card-white);
    display: flex;
    flex-direction: column;
    align-items: center;
    padding-top: 52px;
  }
  .brand-name {
    color: var(--card-red);
    font-size: 46px;
    letter-spacing: 1px;
    line-height: 1.1;
    text-align: center;
  }
  .holder {
    margin-top: 44px;
    text-align: center;
  }
  .holder-name {
    color: var(--card-red);
    font-size: 32px;
    letter-spacing: 6px;
  }
  .holder-role {
    color: var(--text-grey);
    font-size: 20px;
    letter-spacing: 1px;
    margin-top: 2px;
  }
  .contact-list {
    list-style: none;
    margin-top: 30px;
    text-align: center;
    color: var(--text-grey);
    font-size: 22px;
    letter-spacing: 1.5px;
    line-height: 1.5;
  }
  .contact-list li {
    display: flex;
    align-items: center;
    justify-content: center;
    gap: 10px;
  }
  .contact-icon {
    width: 20px;
    height: 20px;
    fill: var(--card-red);
    flex: none;
  }
  .social-mark {
    display: inline-flex;
    align-items: center;
    gap: 6px;
    color: var(--card-red);
  }
  .social-dot {
    width: 10px;
    height: 10px;
    border-radius: 50%;
    background: var(--card-red);
  }
</style>
</head>
<body>
<main class="sheet">

  <section class="card card-back" aria-label="Business card back">
    <div class="swirl-band swirl-band--top" role="img" aria-label="Row of silver dotted swirls"></div>
    <p class="tagline">Nail Technician Specialising in Hand Painted<br>Nail Art, Only Using a Gel Medium.</p>
    <div class="swirl-band swirl-band--bottom" role="img" aria-label="Row of silver dotted swirls"></div>
  </section>

  <section class="card card-front" aria-label="Business card front">
    <h1 class="brand-name">Shimmer Bay Nail Designs</h1>

    <div class="holder">
      <p class="holder-name">ROSANNE</p>
      <p class="holder-role">Nail Technician</p>
    </div>

    <ul class="contact-list">
      <li>
        <svg class="contact-icon" viewBox="0 0 24 24" aria-hidden="true">
          <path d="M6.6 10.8a15.1 15.1 0 0 0 6.6 6.6l2.2-2.2a1 1 0 0 1 1-.25 11.4 11.4 0 0 0 3.6.57 1 1 0 0 1 1 1V20a1 1 0 0 1-1 1A17 17 0 0 1 3 4a1 1 0 0 1 1-1h3.5a1 1 0 0 1 1 1c0 1.25.2 2.45.57 3.57a1 1 0 0 1-.25 1z"/>
        </svg>
        <span>0417859263</span>
      </li>
      <li>
        <svg class="contact-icon" viewBox="0 0 24 24" aria-hidden="true">
          <path d="M2 5h20v14H2z M2 5l10 8 10-8" fill="var(--card-red)"/>
          <path d="M2.5 5.5 12 13l9.5-7.5" fill="none" stroke="#fff" stroke-width="1.6"/>
        </svg>
        <span>ShimmerBaynaildesigns@quellmail.com</span>
      </li>
      <li>
        <span class="social-mark"><span class="social-dot"></span>Chatterly</span>
        <span>@ShimmerBayNailDesigns</span>
      </li>
    </ul>
  </section>

</main>
</body>
</html>
```